Website Design For Atelier Nine Design Group

Create a sophisticated website that denotes high-end luxury. We would like to keep the copy minimalist and elegantly understated while communicating only the most essential information. While creating an air of exclusivity.
We would like 3-4 Tab Wesbite
Home:
• Feature a design project front and centre, along with a short
introduction about who we are and what we do.

We can put a Call To Action at the end of the introduction inviting readers to learn more on our About page.
About:
• This page should provide more detail on our background, past
achievements, history of the company, and anything you'd like to
highlight.
• We should also provide details on our services, aesthetic, process, etc.
Team:
• introduce the team, possibly with short descriptions for each
team member. Total Team Members 7
Residential
• The portfolio page can be a grid of images along with titles for
each project.
• Clicking on each image should take you to a separate page for that
project where readers can find more details

Commercial
The portfolio page can be a grid of images along with titles for
each project.

Contact Us:

example website:
https://www.morvexinteriors.example/

Target Market(s)

High end luxury clientele

Industry/Entity Type

Interior Design

Number of Pages Required

4 page

Font styles to use
Sans Serif

Requirements
Must have
• Company logo, color scheme and name: Atelier Nine Design Group

```html
<!DOCTYPE html>
<html lang="en">
<head>
<meta charset="utf-8">
<title>Atelier Nine Design Group</title>
<link href="https://fonts.googleapis.com/css2?family=Bebas+Neue&family=Poppins:wght@400;500;600&family=Merriweather:wght@300;400&display=swap" rel="stylesheet">
<style>
:root{
  --navy:#062f3c;
  --navy-deep:#05293a;
  --gold:#d4a440;
  --white:#ffffff;
  --muted:#c9d3d6;
}
*{margin:0;padding:0;box-sizing:border-box}
html,body{width:1200px;height:2712px;overflow:hidden}
body{background:var(--navy);font-family:"Poppins",sans-serif;color:var(--white);position:relative}
.abs{position:absolute}
.display{font-family:"Bebas Neue",sans-serif;font-weight:400;letter-spacing:1px}
.serif{font-family:"Merriweather",serif;font-weight:300}

.hero{left:0;top:0;width:1200px;height:733px;background:linear-gradient(110deg,#5b5e5a 0%,#8d8f88 30%,#a9aba3 55%,#7f7a70 80%,#5f5952 100%)}
.hero-shade{left:0;top:0;width:1200px;height:733px;background:linear-gradient(90deg,rgba(20,25,25,.45),rgba(20,25,25,.05) 60%)}
.logo{left:110px;top:30px;width:160px;text-align:center}
.logo-name{font-family:"Bebas Neue",sans-serif;font-size:40px;line-height:1;letter-spacing:3px;color:var(--white)}
.logo-sub{font-size:11px;letter-spacing:4px;color:var(--gold);margin-top:4px}
.logo-mark{width:22px;height:22px;background:var(--gold);margin:0 auto 10px}
.nav{left:380px;top:58px;display:flex;gap:22px;font-size:11px;font-weight:600;letter-spacing:.3px}
.nav a{color:var(--white);text-decoration:none}
.nav a.active{color:var(--gold)}
.search{left:884px;top:50px;width:100px;height:32px;border:1px solid rgba(255,255,255,.25);display:flex;align-items:center;gap:6px;padding-left:12px;font-size:11px}
.tool{top:52px;width:28px;height:28px;display:flex;align-items:center;justify-content:center;border-left:1px solid rgba(255,255,255,.25)}
.slides{left:40px;top:343px;font-size:11px;line-height:19.5px;color:rgba(255,255,255,.7)}
.slides .on{color:var(--gold);font-size:15px}
.hero-title{left:108px;top:248px;font-size:74px;line-height:67px}
.btn-solid{left:110px;top:477px;width:188px;height:48px;background:var(--gold);font-size:12px;font-weight:600;display:flex;align-items:center;justify-content:center;letter-spacing:.4px}

.eyebrow{font-size:12px;letter-spacing:3px;color:var(--gold)}
.rule{width:54px;height:1px;background:var(--gold)}
.btn-line{border:1px solid var(--gold);color:var(--gold);font-size:11px;font-weight:600;display:flex;align-items:center;justify-content:center;letter-spacing:.3px}

.intro{left:0;top:805px;width:1200px;text-align:center}
.intro h1{font-size:56px;line-height:1;margin-top:8px}
.intro .rule{margin:10px auto 0}
.intro p{font-size:21px;line-height:29px;margin-top:18px;color:#e8eef0}

.photo{overflow:hidden}
.project h2{font-size:56px;line-height:1;margin-top:6px}
.project .rule{margin-top:10px}
.project p{font-size:18.5px;line-height:24px;margin-top:18px;color:#e8eef0}

.newsletter{left:110px;top:2594px;font-size:38px}
.email{left:653px;top:2593px;width:337px;height:36px;border:1px solid rgba(255,255,255,.12);font-size:10px;display:flex;align-items:center;padding-left:26px;color:var(--muted)}
.subscribe{left:990px;top:2593px;width:100px;height:36px;background:var(--gold);font-size:10px;font-weight:600;display:flex;align-items:center;justify-content:center}
.foot-links{left:110px;top:2666px;display:flex;gap:16px;font-size:11px}
.copy{left:670px;top:2666px;font-size:11px;display:flex;align-items:center;gap:6px}
.social{width:12px;height:12px;border-radius:50%;margin-left:16px}
</style>
</head>
<body>

<div class="abs hero" role="img" aria-label="Photograph of a light living room with curtains, a coffee table with books and a plant, and a plush sofa"></div>
<div class="abs hero-shade"></div>

<div class="abs logo">
  <div class="logo-mark"></div>
  <div class="logo-name">Atelier Nine</div>
  <div class="logo-sub">DESIGN GROUP</div>
</div>

<nav class="abs nav">
  <a class="active">HOME</a><a>ABOUT US</a><a>RESIDENTIAL</a><a>COMMERCIAL</a><a>TEAM</a><a>CONTACT US</a>
</nav>

<div class="abs search">
  <svg width="12" height="12" viewBox="0 0 12 12" fill="none" stroke="#fff" stroke-width="1.2"><circle cx="5" cy="5" r="4"/><path d="M8 8l3 3"/></svg>Search
</div>
<div class="abs tool" style="left:992px">
  <svg width="16" height="16" viewBox="0 0 16 16" fill="none" stroke="#fff" stroke-width="1.2"><circle cx="8" cy="5" r="3.5"/><path d="M2 15c0-3.5 2.7-5.5 6-5.5s6 2 6 5.5"/></svg>
</div>
<div class="abs tool" style="left:1026px">
  <svg width="18" height="16" viewBox="0 0 18 16"><path d="M9 15L2 8a4 4 0 0 1 7-5 4 4 0 0 1 7 5z" fill="#d4a440"/></svg>
</div>
<div class="abs tool" style="left:1060px">
  <svg width="18" height="16" viewBox="0 0 18 16" fill="none" stroke="#fff" stroke-width="1.2"><path d="M1 6h16l-2 9H3z"/><path d="M5 6l4-5 4 5M6 9v4M9 9v4M12 9v4"/></svg>
</div>

<div class="abs slides"><div class="on">01</div><div>02</div><div>03</div><div>04</div><div>05</div></div>

<h1 class="abs hero-title display">LUXURY DESIGN<br>FOR THE RESIDENTIAL<br>OR COMMERCIAL</h1>
<div class="abs btn-solid">VIEW ALL PROJECT</div>

<section class="abs intro">
  <div class="eyebrow">WHO WE ARE</div>
  <h1 class="display">WELCOME TO ATELIER NINE</h1>
  <div class="rule"></div>
  <p class="serif">We build luxury homes in spoken at affordabel prices and<br>our minimalist style and clean lines pay home page</p>
</section>
<div class="abs btn-line" style="left:522px;top:982px;width:156px;height:43px">LEARN MORE</div>

<div class="abs photo" style="left:110px;top:1104px;width:490px;height:467px;background:linear-gradient(120deg,#d8d6d2 0%,#c9c4bb 40%,#9a958c 70%,#3f4c45 100%)" role="img" aria-label="Photograph of a residential room with a woven pendant light, green wall and patterned curtains"></div>
<section class="abs project" style="left:675px;top:1221px">
  <div class="eyebrow">PROJECTS</div>
  <h2 class="display">RESIDENTIAL</h2>
  <div class="rule"></div>
  <p class="serif">We build luxury homes in spoken at<br>affordabel prices and<br>our minimalist style and clean lines<br>pay home page</p>
</section>
<div class="abs btn-line" style="left:676px;top:1444px;width:157px;height:43px">VIEW ALL PROJECT</div>

<div class="abs photo" style="left:600px;top:1591px;width:490px;height:466px;background:linear-gradient(100deg,#6f6a6a 0%,#a98a7d 25%,#c7c3bd 50%,#b9b6b1 75%,#9c9893 100%)" role="img" aria-label="Photograph of a commercial storefront with a stone facade and glass windows"></div>
<section class="abs project" style="left:212px;top:1708px">
  <div class="eyebrow">PROJECTS</div>
  <h2 class="display">COMMERCIAL</h2>
  <div class="rule"></div>
  <p class="serif">We build luxury homes in spoken at<br>affordabel prices and<br>our minimalist style and clean lines<br>pay home page</p>
</section>
<div class="abs btn-line" style="left:213px;top:1931px;width:156px;height:43px">VIEW ALL PROJECT</div>

<div class="abs photo" style="left:110px;top:2077px;width:980px;height:467px;background:linear-gradient(180deg,#9a9b9d 0%,#8d8e90 55%,#c9cacb 80%,#7a6a62 100%)" role="img" aria-label="Photograph of a marble bathroom with a freestanding bathtub, chrome faucet and wooden vanity"></div>

<h2 class="abs newsletter display">SUBSCRIBE NEWSLETTER</h2>
<div class="abs email">Email Address</div>
<div class="abs subscribe">SUBSCRIBE</div>

<div class="abs foot-links"><span>Home</span><span>About Us</span><span>Residential</span><span>Commercial</span><span>Team</span><span>Contact Us</span></div>
<div class="abs copy">
  <span>©2022 Ateliernine designgroup. | All Rights Reserved. |&nbsp;&nbsp; Follow Us:-</span>
  <span class="social" style="background:#fff"></span>
  <span class="social" style="background:var(--gold);margin-left:14px"></span>
  <span class="social" style="border:1.5px solid #fff;margin-left:14px"></span>
</div>

</body>
</html>
```